MODELS AGENCY NEW YEAR 2026 CARD

A 10 cm x 21 cm horizontal New Year card for clients of our 2 models agencies, Pebblio (kids) and Vantriko (actors and adults) (logo in the jobs).

Side A of the card: creative mission:
-text: 2026
-text: Peace and Love
-Studio or movie set atmosphere
-tone of voice: optimistic, positive, colorful

Side B:
(name of 4 people of the agency:)
Odette, Anne-Solveig, Hélodie & Pierre-Olivier,
(2 logos)
Pebblio & VanTriko
(Adres)
Rue des Orvilliers 42 b5 - 1187 Bruxelles - Belgique

Target Market(s)

Movie directors, photographers

Industry/Entity Type

Fashion, advertising & Movies

Requirements
Must have
• SEE TEXT IN BRIEFING

```html
<!DOCTYPE html>
<html lang="fr">
<head>
<meta charset="utf-8">
<title>Vantriko &amp; Pebblio — New Year 2026</title>
<link rel="stylesheet" href="https://fonts.googleapis.com/css2?family=Abril+Fatface&family=Montserrat:wght@500;600;700&display=swap">
<style>
  :root {
    --page: #ffffff;
    --red: #c8001a;
    --red-deep: #6b0006;
    --red-bright: #e0001c;
    --ink: #0b0b0b;
    --cream: #e6ddd8;
    --plum: #3f1d5c;
    --orange: #ec5a12;
    --sky: #1f9ad8;
    --rule: rgba(255,255,255,0.35);
  }
  * { margin: 0; padding: 0; box-sizing: border-box; }
  html, body { width: 1200px; height: 1200px; overflow: hidden; background: var(--page); }
  body { position: relative; font-family: "Montserrat", sans-serif; }

  .card {
    position: absolute; left: 104px; width: 999px; height: 476px;
    background: var(--page);
    box-shadow: 0 10px 30px rgba(0,0,0,0.12);
    overflow: hidden;
  }
  .card--front { top: 96px; }
  .card--back { top: 639px; height: 475px; }

  /* Front */
  .year { position: absolute; left: 0; top: 0; width: 162px; height: 476px; }
  .studio-scene {
    position: absolute; left: 162px; top: 0; width: 837px; height: 476px;
    background:
      radial-gradient(ellipse 38% 55% at 48% 55%, #d4001c 0%, #9a0010 45%, rgba(60,0,4,0) 80%),
      linear-gradient(90deg, #0c0c0c 0%, #2a0204 22%, #7a000b 45%, #7a000b 60%, #1a0202 82%, #0c0c0c 100%);
  }
  .greeting {
    position: absolute; font-family: "Abril Fatface", serif; color: var(--cream);
    line-height: 1; font-size: 68px;
  }
  .greeting--peace { left: 603px; top: 138px; }
  .greeting--love { left: 650px; top: 200px; }
  .greeting__amp { color: var(--ink); font-size: 82px; margin-right: 8px; vertical-align: -6px; }

  /* Back */
  .team-panel {
    position: absolute; left: 0; top: 0; width: 611px; height: 475px;
    background: radial-gradient(ellipse 70% 75% at 36% 58%, var(--red-bright) 0%, #a5000f 45%, var(--red-deep) 100%);
  }
  .team { list-style: none; position: absolute; left: 68px; top: 93px; width: 427px; }
  .team__name {
    font-family: "Abril Fatface", serif; color: #fff; font-size: 42px; line-height: 1;
    border-bottom: 2px solid var(--rule);
  }
  .team__name:nth-child(1) { padding: 0 0 9px; }
  .team__name:nth-child(2) { padding: 11px 0 14px; }
  .team__name:nth-child(3) { padding: 10px 0 7px; }
  .team__name:nth-child(4) { padding: 10px 0 12px; }
  .address {
    position: absolute; left: 68px; top: 380px; color: #fff;
    font-weight: 600; font-size: 16.5px; letter-spacing: 0.2px;
  }

  .agencies { position: absolute; left: 611px; top: 0; width: 388px; height: 475px; }
  .agency { position: absolute; left: 0; width: 100%; text-align: center; }
  .agency--adults { top: 97px; }
  .agency--kids { top: 293px; }
  .agency__name {
    font-family: "Montserrat", sans-serif; font-weight: 700; font-size: 40px;
    line-height: 1; color: var(--plum); letter-spacing: 1px;
  }
  .agency__tagline { margin-top: 8px; font-size: 9.5px; letter-spacing: 1.6px; font-weight: 500; }
  .agency--adults .agency__tagline { color: var(--plum); }
  .agency--kids .agency__tagline { color: var(--plum); }
  .agency__since { margin-top: 44px; font-size: 7.5px; color: var(--plum); letter-spacing: 0.3px; }
  .agency__dot { display: inline-block; width: 10px; height: 10px; border-radius: 50%; margin-right: 10px; vertical-align: 6px; }
  .agency--adults .agency__dot { background: var(--orange); }
  .agency--kids .agency__dot { background: var(--sky); }
</style>
</head>
<body>
  <section class="card card--front">
    <svg class="year" viewBox="0 0 162 476" aria-label="2026">
      <defs>
        <linearGradient id="yearFade" gradientUnits="userSpaceOnUse" x1="0" y1="-120" x2="0" y2="0">
          <stop offset="0" stop-color="#c8001a"/>
          <stop offset="0.55" stop-color="#c8001a"/>
          <stop offset="1" stop-color="#0b0b0b"/>
        </linearGradient>
      </defs>
      <text transform="translate(160,448) rotate(-90)" font-family="Abril Fatface, serif" font-size="172"
            fill="url(#yearFade)" textLength="413" lengthAdjust="spacingAndGlyphs">2026</text>
    </svg>
    <div class="studio-scene" role="img" aria-label="Photo studio set with red backdrop, two softbox lights, a white armchair with red cushion, knitted blanket, Santa hat, small Christmas trees and wrapped gifts"></div>
    <div class="greeting greeting--peace">Peace</div>
    <div class="greeting greeting--love"><span class="greeting__amp">&amp;</span>Love</div>
  </section>

  <section class="card card--back">
    <div class="team-panel">
      <ul class="team">
        <li class="team__name">Odette</li>
        <li class="team__name">Anne-Solveig</li>
        <li class="team__name">Hélodie</li>
        <li class="team__name">Pierre-Olivier</li>
      </ul>
      <p class="address">Rue des Orvilliers 42 b5 - 1187 Bruxelles - Belgique</p>
    </div>
    <div class="agencies">
      <div class="agency agency--adults">
        <div class="agency__name"><span class="agency__dot"></span>VanTriko</div>
        <div class="agency__tagline">PEOPLE, ACTORS &amp; MODELS AGENCY</div>
        <div class="agency__since">– SINCE 2000 –</div>
      </div>
      <div class="agency agency--kids">
        <div class="agency__name"><span class="agency__dot"></span>Pebblio</div>
        <div class="agency__tagline">CHILDREN MODELS AGENCY</div>
        <div class="agency__since">– SINCE 1982 –</div>
      </div>
    </div>
  </section>
</body>
</html>
```